Tambrook copiers needs flyer for the Corvane Trade expo

A flyer to hand out had the Corvane Trade expo in Melbourne. I am am happy with the layout attached , but i need a claen ( no watermarks) background for the top half of the fist page. It must have one of the copiers attached in the photo

```html
<!DOCTYPE html>
<html lang="en">
<head>
<meta charset="utf-8">
<title>Tambrook Copiers – Show Special</title>
<link rel="stylesheet" href="https://fonts.googleapis.com/css2?family=Bebas+Neue&family=Montserrat:wght@400;500;700;800&family=Poppins:wght@300&display=swap">
<style>
  :root {
    --ink: #141414;
    --red: #d6202a;
    --grey-light: #c9c7ce;
    --grey-mid: #a9a7b0;
    --yellow: #fdd20b;
    --amber: #f7b414;
    --white: #ffffff;
  }
  * { margin: 0; padding: 0; box-sizing: border-box; }
  html, body { width: 940px; height: 1200px; overflow: hidden; background: #8a8a8a; }
  .flyer {
    position: relative;
    width: 940px;
    height: 1200px;
    overflow: hidden;
    font-family: "Montserrat", sans-serif;
    color: var(--ink);
    background: var(--yellow);
  }
  .hero-backdrop {
    position: absolute; left: 0; top: 0; width: 940px; height: 620px;
    background: linear-gradient(160deg, #d9d7dd 0%, var(--grey-light) 40%, var(--grey-mid) 75%, #cfcdd4 100%);
  }
  .price-panel { position: absolute; left: 0; top: 0; width: 940px; height: 1200px; }
  .show-tab {
    position: absolute; left: 245px; top: 18px; width: 372px; height: 56px;
    background: var(--red); color: var(--white);
    font-family: "Montserrat", sans-serif; font-weight: 700; font-size: 22px;
    letter-spacing: 0.38em; text-indent: 0.38em; text-align: center; line-height: 56px;
  }
  .headline {
    position: absolute; left: 100px; top: 110px;
    font-family: "Bebas Neue", sans-serif; font-weight: 400; font-size: 200px; line-height: 0.64;
    color: var(--ink); white-space: nowrap;
  }
  .copier-photo {
    position: absolute; left: 72px; top: 362px; width: 318px; height: 538px;
    background: linear-gradient(180deg, #e9e9ec 0%, #c3c7d2 14%, #3f5a85 24%, #e3e4e7 38%, #d9dadd 100%);
    border-radius: 6px;
  }
  .features { position: absolute; left: 364px; top: 398px; list-style: none; }
  .features li {
    display: flex; align-items: center; gap: 12px; height: 34px;
    font-family: "Poppins", sans-serif; font-weight: 300; font-size: 24px;
    margin-bottom: 20px; color: #222;
  }
  .features svg { width: 28px; height: 28px; flex: none; }
  .plan { position: absolute; }
  .plan-title { font-weight: 800; font-size: 29px; line-height: 35px; letter-spacing: -0.01em; }
  .plan-price { font-family: "Bebas Neue", sans-serif; line-height: 74px; height: 74px; margin-top: 4px; white-space: nowrap; }
  .plan-price .amount { color: var(--red); font-size: 74px; }
  .plan-price .term { font-size: 40px; margin-left: 8px; }
  .plan-details { list-style: none; font-size: 14.5px; font-weight: 500; }
  .plan-details li { height: 28px; line-height: 28px; white-space: nowrap; }
  .plan-details .figure { font-family: "Bebas Neue", sans-serif; color: var(--red); font-size: 27px; line-height: 0; vertical-align: -2px; }
  .plan-details .unit { font-size: 19px; }
  .plan-medium { left: 480px; top: 573px; }
  .plan-colour { left: 493px; top: 790px; }
  .plan-small { left: 116px; top: 935px; }
  .brand {
    position: absolute; left: 540px; top: 1048px;
    display: flex; align-items: center; gap: 14px;
    font-family: "Montserrat", sans-serif; font-weight: 800; font-size: 44px;
    line-height: 1; color: var(--ink); text-transform: uppercase;
  }
  .brand-square { width: 26px; height: 26px; background: var(--red); }
</style>
</head>
<body>
<main class="flyer">
  <div class="hero-backdrop" role="img" aria-label="Soft-focus photograph of a bright office interior"></div>
  <svg class="price-panel" viewBox="0 0 940 1200" aria-hidden="true">
    <polygon points="0,575 940,540 940,1200 0,1200" fill="var(--yellow)"/>
    <polygon points="0,900 940,650 940,1000 0,1150" fill="var(--amber)" opacity="0.45"/>
  </svg>

  <div class="show-tab">SHOW SPECIAL</div>
  <h1 class="headline">NO LOCK-IN<br>CONTRACTS</h1>

  <div class="copier-photo" role="img" aria-label="Photograph of a freestanding A3/A4 colour office copier"></div>

  <ul class="features">
    <li><svg viewBox="0 0 30 30"><circle cx="14" cy="16" r="11" fill="none" stroke="var(--red)" stroke-width="3"/><path d="M8 15l6 6 12-15" fill="none" stroke="var(--red)" stroke-width="4" stroke-linecap="round"/></svg>Freestanding A3/A4 Colour Printer.</li>
    <li><svg viewBox="0 0 30 30"><circle cx="14" cy="16" r="11" fill="none" stroke="var(--red)" stroke-width="3"/><path d="M8 15l6 6 12-15" fill="none" stroke="var(--red)" stroke-width="4" stroke-linecap="round"/></svg>Includes All Toner &amp; Service.</li>
    <li><svg viewBox="0 0 30 30"><circle cx="14" cy="16" r="11" fill="none" stroke="var(--red)" stroke-width="3"/><path d="M8 15l6 6 12-15" fill="none" stroke="var(--red)" stroke-width="4" stroke-linecap="round"/></svg>Change plans to suit your needs.</li>
  </ul>

  <section class="plan plan-medium">
    <h2 class="plan-title">Medium Business Plan</h2>
    <p class="plan-price"><span class="amount">$210</span><span class="term">+GST PER MONTH</span></p>
    <ul class="plan-details">
      <li>Includes printer &amp; 6000 B&amp;W pages p/m.</li>
      <li>Excess B&amp;W pages are <span class="figure">3.5<span class="unit">c</span></span> +GST.</li>
      <li>Colour pages are <span class="figure">9<span class="unit">c</span></span> +GST.</li>
    </ul>
  </section>

  <section class="plan plan-colour">
    <h2 class="plan-title">Discounted Colour Plan</h2>
    <p class="plan-price"><span class="amount">$280</span><span class="term">+GST PER MONTH</span></p>
    <ul class="plan-details">
      <li>Includes printer &amp; 4000 colour pages p/m.</li>
      <li>Excess colour pages are <span class="figure">7<span class="unit">c</span></span> +GST.</li>
      <li>Discounts for high volume users.</li>
      <li>Less than <span class="figure">$9.50</span> a day.</li>
    </ul>
  </section>

  <section class="plan plan-small">
    <h2 class="plan-title">Small Business Plan</h2>
    <p class="plan-price"><span class="amount">$150</span><span class="term">+GST PER MONTH</span></p>
    <ul class="plan-details">
      <li>Includes printer &amp; 3000 B&amp;W pages p/m.</li>
      <li>Excess B&amp;W pages are <span class="figure">5<span class="unit">c</span></span> +GST.</li>
      <li>Colour pages are are <span class="figure">9<span class="unit">c</span></span> +GST.</li>
      <li>That's only <span class="figure">$5</span> a day.</li>
    </ul>
  </section>

  <div class="brand"><span class="brand-square"></span><span>Tambrook<br>Copiers</span></div>
</main>
</body>
</html>
```